Auto glazing business card design

need a business card design for my company, the logo will be provided with an inspirational design as well.
It is for an auto glazing business in Australia.
I would like to have the basic details on the card as my name, phone number, email adress and website.
I suppose the challenge will be to fit a long email adress on a small business card.

Target Market(s)

autoglazing customers, retail mostly

Industry/Entity Type

auto glazing

Contact Information for Business Card

logo, name, phone, email and website

Colors
0054AA
0677BA
7BADD7
CADEEF
E8F1F8
0094D4
00A9DD
6FCCEA
C7EBF8
E9F6FB

Requirements
Must have
• logo, business details, maybe QR code

```html
<!DOCTYPE html>
<html lang="en">
<head>
<meta charset="utf-8">
<title>Clearpath Mobile Glazing – Business Card</title>
<link href="https://fonts.googleapis.com/css2?family=Lato:wght@400;700&display=swap" rel="stylesheet">
<style>
  :root {
    --backdrop: #8f8f8f;
    --navy: #061b34;
    --teal: #1b8db8;
    --ink: #2a2f36;
    --white: #ffffff;
  }
  * { margin: 0; padding: 0; box-sizing: border-box; }
  html, body { width: 1200px; height: 1000px; overflow: hidden; }
  body { background: var(--backdrop); font-family: "Lato", sans-serif; position: relative; }

  .card {
    position: absolute; left: 290px; width: 629px; height: 359px;
    border-radius: 23px; overflow: hidden;
    box-shadow: 0 2px 6px rgba(0,0,0,0.25);
  }
  .card--front { top: 97px; background: var(--white); }
  .card--back { top: 533px; background: var(--navy); }

  .brand { position: absolute; text-align: center; font-weight: 700; text-transform: uppercase; }
  .brand__mark { display: block; margin: 0 auto 10px; border-radius: 50%; }
  .brand__name { display: block; letter-spacing: 0.22em; line-height: 1.25; }

  .card--front .brand { left: 390px; top: 38px; width: 190px; color: var(--navy); }
  .card--front .brand__mark { width: 46px; height: 46px; background: var(--navy); }
  .card--front .brand__name { font-size: 16px; }

  .card--back .brand { left: 0; right: 0; top: 95px; color: var(--white); }
  .card--back .brand__mark { width: 80px; height: 80px; background: var(--white); margin-bottom: 18px; }
  .card--back .brand__name { font-size: 30px; }

  .holder { position: absolute; left: 34px; top: 176px; }
  .holder__name { font-size: 29px; font-weight: 700; color: var(--navy); letter-spacing: 0.01em; line-height: 1; }
  .holder__role { font-size: 15px; color: var(--teal); margin-top: 6px; }

  .divider { position: absolute; left: 36px; top: 240px; width: 558px; height: 1.5px; background: var(--navy); }

  .contacts { position: absolute; left: 34px; top: 254px; list-style: none; }
  .contacts li { display: flex; align-items: center; height: 19.4px; font-size: 14.5px; color: var(--ink); }
  .contacts svg { width: 11px; height: 11px; margin-right: 10px; fill: var(--teal); }

  .company { position: absolute; right: 35px; top: 253px; text-align: right; font-size: 14.5px; color: var(--ink); line-height: 19.4px; }
  .company__name { color: var(--teal); font-weight: 700; }
</style>
</head>
<body>
  <section class="card card--front">
    <div class="brand">
      <span class="brand__mark"></span>
      <span class="brand__name">Clearpath<br>Mobile Glazing</span>
    </div>

    <div class="holder">
      <h1 class="holder__name">DANIEL REEVE</h1>
      <p class="holder__role">Founder &amp; CEO</p>
    </div>

    <div class="divider"></div>

    <ul class="contacts">
      <li><svg viewBox="0 0 12 12"><path d="M2.5 1l2 2.2-1 1.3a7 7 0 0 0 4 4l1.3-1 2.2 2-1.3 1.8C5.5 11 1 6.5.7 2.3z"/></svg>(555) 014-2290</li>
      <li><svg viewBox="0 0 12 12"><path d="M3 .5h6a1 1 0 0 1 1 1v9a1 1 0 0 1-1 1H3a1 1 0 0 1-1-1v-9a1 1 0 0 1 1-1zm.5 1.5v7h5V2zM6 9.6a.6.6 0 1 0 0 1.2.6.6 0 0 0 0-1.2z"/></svg>(555) 014-2291</li>
      <li><svg viewBox="0 0 12 12"><path d="M3 .5h6v3H3zM1 4.5h10v5H9.5v-2h-7v2H1zM3 8.5h6v3H3z"/></svg>(555) 014-2292</li>
      <li><svg viewBox="0 0 12 12"><path d="M.5 2.5h11v7H.5zM1.5 3.2L6 6.7l4.5-3.5v.9L6 7.6 1.5 4.1z" fill-rule="evenodd"/></svg>hello@clearpathmobileglazing.com</li>
    </ul>

    <div class="company">
      <p class="company__name">Clearpath Mobile Glazing</p>
      <p>12 Harbour Lane, Brookvale</p>
      <p>NSW, Australia, 2100</p>
      <p>www.clearpathmobileglazing.com</p>
    </div>
  </section>

  <section class="card card--back">
    <div class="brand">
      <span class="brand__mark"></span>
      <span class="brand__name">Clearpath<br>Mobile Glazing</span>
    </div>
  </section>
</body>
</html>
```